Corwenna Foundation is a new grant making charity set up in the UK.

Having got a logo, we now need a website to go with it. We have worked out the text which people are going to need in order to then apply for grants. But having found out what we require they will probably need to go away and think about it.
We have to be careful of what images we use. So I have uploaded some images that we like. We are also going to be adding more pages almost immediately so need to think about the images for these.
I know basic wordpress so I will be able to add new pages/make alterations in future.
Updates
The website does need to be coded in Wordpress so that I can maintain it afterwards.
Corwenna
Brief changed to provide more money and we have also provided more possible pictures. And generally more explanation.
Target Market(s)
departments in universities, other charities doing work on relief of pain, people working in health service departments
Industry/Entity Type
Health Charity
Coding
Coded - Design and coding required
Number of Pages Required
4 page
Look and feel
Each slider illustrates characteristics of the customer's brand and the style your logo design should communicate.

```html
<!DOCTYPE html>
<html lang="en">
<head>
<meta charset="utf-8">
<title>Corwenna Foundation</title>
<link rel="stylesheet" href="https://fonts.googleapis.com/css2?family=Rubik:wght@500;600;700&family=Poppins:wght@400;500;600&display=swap">
<style>
:root{
  --blue:#1a63d6;
  --blue-deep:#0b3fa6;
  --ink:#111;
  --grey-text:#666;
  --panel:#efefef;
  --frame:#bdbdbd;
  --white:#fff;
  --black:#050505;
}
*{box-sizing:border-box;margin:0;padding:0}
html,body{width:1200px;height:2655px;overflow:hidden;background:var(--white)}
body{font-family:"Poppins",sans-serif;color:var(--ink);position:relative}
.page{position:relative;width:1200px;height:2655px;overflow:hidden}
.abs{position:absolute}

/* hero */
.hero-bg{left:0;top:0;width:1200px;height:640px}
.brand{left:97px;top:15px;display:flex;align-items:center;gap:8px;color:var(--blue);font-family:"Rubik",sans-serif;font-weight:600;font-size:17px;letter-spacing:.5px;line-height:1.05}
.brand-mark{width:28px;height:28px;border:3px solid var(--blue)}
.brand.footer-brand{left:0;width:1200px;top:2410px;justify-content:center;font-size:20px}
.nav{top:13px;left:855px;display:flex;gap:22px;font-size:12.5px;color:var(--white)}
.nav a{color:inherit;text-decoration:none;padding:0 4px 8px}
.nav a.active{border-bottom:2px solid var(--white)}
.hero-title{left:61px;top:218px;width:500px;font-family:"Rubik",sans-serif;font-size:33px;line-height:41px;font-weight:600;color:var(--white)}
.hero-text{left:61px;top:353px;width:340px;font-size:12.5px;line-height:20px;color:var(--white)}
.hero-reg{left:61px;top:405px;font-size:12.5px;color:var(--white)}
.hero-btn{left:60px;top:450px;width:127px;height:37px;background:var(--white)}

/* about */
.about{left:0;top:637px;width:1200px;height:391px;background:var(--panel)}
.section-title{width:1200px;left:0;text-align:center;font-family:"Rubik",sans-serif;font-weight:700}
.section-title span{color:var(--blue)}
.about-title{top:692px;font-size:34px}
.card-label{width:300px;text-align:center;font-size:14.5px;line-height:20px;font-family:"Rubik",sans-serif;font-weight:500}
.arrow-tri{width:0;height:0;border-top:9px solid transparent;border-bottom:9px solid transparent}

/* welcome */
.welcome-kicker{top:1110px;left:0;width:1200px;text-align:center;font-family:"Rubik",sans-serif;font-weight:600;font-size:14px;color:#444}
.welcome-title{top:1136px;font-size:38px}
.center-text{left:0;width:1200px;text-align:center;font-size:12.5px;line-height:19.5px;color:var(--grey-text)}
.center-text p{width:460px;margin:0 auto}
.slide-card{left:338px;top:1286px;width:527px;height:301px;border:2px solid var(--blue)}
.slide-title{left:523px;top:1339px;font-family:"Rubik",sans-serif;font-weight:500;font-size:18.5px}
.slide-body{left:523px;top:1373px;width:285px;font-size:12px;line-height:19.5px;color:var(--grey-text)}
.slide-btn{left:743px;top:1532px;width:122px;height:33px;background:var(--blue);color:var(--white);font-family:"Rubik",sans-serif;font-weight:600;font-size:13px;display:flex;align-items:center;justify-content:center;padding-left:10px;clip-path:polygon(0 0,100% 0,100% 100%,0 100%,12px 50%)}
.chev{font-size:28px;color:#333;line-height:1}

/* contact */
.contact-title{top:1758px;font-size:38px;color:var(--white)}
.contact-sub{left:0;width:1200px;top:1808px;text-align:center;font-size:12.5px;line-height:20px;color:var(--white)}
.field{border:1px solid rgba(255,255,255,.85);color:var(--white);font-size:12.5px;padding:10px 9px;width:225px;height:38px}
.field.tall{height:60px}
.submit{left:613px;top:1945px;width:225px;height:60px;background:var(--white);display:flex;align-items:center;justify-content:center;font-family:"Rubik",sans-serif;font-weight:600;font-size:15px;color:var(--ink)}

/* aim */
.aim-bg{left:0;top:2083px;width:1200px;height:240px}
.aim-title{top:2120px;font-size:26px;line-height:34px;font-weight:500;color:var(--ink)}
.aim-btn{left:536px;top:2214px;width:128px;height:37px;background:var(--blue);color:var(--white);font-family:"Rubik",sans-serif;font-weight:600;font-size:15px;display:flex;align-items:center;justify-content:center}

/* footer */
.foot-links{top:2470px;left:0;width:1200px;display:flex;justify-content:center;gap:20px;color:var(--white);font-size:12.5px}
.foot-rule{left:180px;top:2502px;width:840px;height:1px;background:#555}
.foot-item{display:flex;align-items:center;gap:10px;color:var(--white);font-size:12.5px;line-height:19px;top:2520px}
.icon-box{width:39px;height:39px;border:1px solid var(--blue);display:flex;align-items:center;justify-content:center;flex:none}
.copy-rule{left:0;top:2622px;width:1200px;height:1px;background:#333}
.copy{left:0;width:1200px;top:2631px;text-align:center;color:var(--white);font-size:12px}
</style>
</head>
<body>
<div class="page">

  <!-- HERO -->
  <svg class="abs hero-bg" viewBox="0 0 1200 640">
    <defs>
      <linearGradient id="heroBlue" x1="0" y1="0" x2="1" y2="1">
        <stop offset="0" stop-color="#1c6ee0"/>
        <stop offset="1" stop-color="#1557c8"/>
      </linearGradient>
      <linearGradient id="heroPhotoBase" x1="0" y1="0" x2="1" y2="1">
        <stop offset="0" stop-color="#1d7ef0"/>
        <stop offset="0.5" stop-color="#1448b8"/>
        <stop offset="1" stop-color="#0a2680"/>
      </linearGradient>
      <radialGradient id="heroGlowKnee" cx="700" cy="300" r="170" gradientUnits="userSpaceOnUse">
        <stop offset="0" stop-color="#ffb347" stop-opacity=".95"/>
        <stop offset="0.35" stop-color="#f0702a" stop-opacity=".7"/>
        <stop offset="1" stop-color="#f0702a" stop-opacity="0"/>
      </radialGradient>
      <radialGradient id="heroGlowLeg" cx="640" cy="520" r="150" gradientUnits="userSpaceOnUse">
        <stop offset="0" stop-color="#ff8a3a" stop-opacity=".7"/>
        <stop offset="1" stop-color="#ff8a3a" stop-opacity="0"/>
      </radialGradient>
      <radialGradient id="heroGlowBody" cx="950" cy="180" r="260" gradientUnits="userSpaceOnUse">
        <stop offset="0" stop-color="#4fb4ff" stop-opacity=".55"/>
        <stop offset="1" stop-color="#4fb4ff" stop-opacity="0"/>
      </radialGradient>
      <clipPath id="heroClip"><polygon points="560,0 1200,0 1200,640 165,640"/></clipPath>
    </defs>
    <rect width="1200" height="640" fill="url(#heroBlue)"/>
    <g clip-path="url(#heroClip)" role="img" aria-label="Photo: woman seated holding a glowing, painful knee in x-ray style">
      <rect width="1200" height="640" fill="url(#heroPhotoBase)"/>
      <rect width="1200" height="640" fill="url(#heroGlowBody)"/>
      <rect width="1200" height="640" fill="url(#heroGlowLeg)"/>
      <rect width="1200" height="640" fill="url(#heroGlowKnee)"/>
    </g>
    <polygon points="31,0 361,0 193,147" fill="#fff"/>
  </svg>

  <div class="abs brand"><span class="brand-mark"></span><span>CORWENNA<br>FOUNDATION</span></div>

  <nav class="abs nav">
    <a class="active" href="#">Home</a><a href="#">About Us</a><a href="#">Grants</a><a href="#">Contact Us</a>
  </nav>

  <h1 class="abs hero-title">Corwenna Foundation is a grant making charity set up in the UK in 2021</h1>
  <p class="abs hero-text">The main aim of Corwenna Foundation is to reduce the suffering caused by chronic pain.</p>
  <p class="abs hero-reg">Charity registration number 1187654.</p>
  <div class="abs hero-btn"></div>

  <!-- ABOUT -->
  <div class="abs about"></div>
  <svg class="abs" style="left:0;top:637px" width="170" height="150" aria-hidden="true"><polygon points="0,0 165,0 0,145" fill="#1a63d6"/></svg>
  <h2 class="abs section-title about-title">ABOUT <span>US</span></h2>

  <div class="abs arrow-tri" style="left:60px;top:831px;border-right:9px solid var(--blue)"></div>
  <div class="abs arrow-tri" style="left:1123px;top:831px;border-left:9px solid var(--blue)"></div>

  <p class="abs card-label" style="left:139px;top:749px">Who are the trustees of Corwenna Foundation?</p>
  <svg class="abs" style="left:144px;top:805px" width="290" height="140">
    <defs>
      <linearGradient id="pillsTone" x1="0" y1="0" x2="1" y2="0.6">
        <stop offset="0" stop-color="#f0a020"/>
        <stop offset="0.3" stop-color="#e88a1a"/>
        <stop offset="0.5" stop-color="#f4efe6"/>
        <stop offset="0.7" stop-color="#8a3a2a"/>
        <stop offset="1" stop-color="#2e2b28"/>
      </linearGradient>
    </defs>
    <polygon points="0,0 289,0 145,139" fill="url(#pillsTone)" role="img" aria-label="Photo: pills and medicine vials"/>
  </svg>

  <svg class="abs" style="left:455px;top:774px" width="290" height="140">
    <defs>
      <linearGradient id="medTone" x1="0" y1="0" x2="1" y2="1">
        <stop offset="0" stop-color="#4b8ff0"/>
        <stop offset="0.5" stop-color="#2a6ddc"/>
        <stop offset="1" stop-color="#1752c2"/>
      </linearGradient>
    </defs>
    <polygon points="0,139 288,139 144,0" fill="url(#medTone)" role="img" aria-label="Photo: medical team, blue tinted"/>
  </svg>
  <p class="abs card-label" style="left:453px;top:929px">Who are the medical advisers to Corwenna Foundation?</p>

  <p class="abs card-label" style="left:739px;top:749px">How much money does Corwenna Foundation have?</p>
  <svg class="abs" style="left:755px;top:805px" width="290" height="140">
    <defs>
      <radialGradient id="moneyTone" cx="0.5" cy="0.35" r="0.6">
        <stop offset="0" stop-color="#c9a48a"/>
        <stop offset="0.45" stop-color="#8c8576"/>
        <stop offset="1" stop-color="#5a5a52"/>
      </radialGradient>
    </defs>
    <polygon points="0,0 289,0 145,139" fill="url(#moneyTone)" role="img" aria-label="Photo: woman meditating among floating banknotes"/>
  </svg>

  <!-- WELCOME -->
  <p class="abs welcome-kicker">WELCOME TO</p>
  <h2 class="abs section-title welcome-title">CORWENNA&nbsp; <span>FOUNDATION</span></h2>
  <div class="abs center-text" style="top:1186px">
    <p>Grants will almost entirely be provided for research or education into pain management, or the prevention of pain.</p>
    <p style="margin-top:6px">The main categories of funding for pain research or education will be as follows.</p>
  </div>

  <!-- faded side slides -->
  <svg class="abs" style="left:0;top:1284px" width="230" height="306">
    <defs>
      <radialGradient id="runnerTone" cx="0.5" cy="0.45" r="0.55">
        <stop offset="0" stop-color="#c9d8ee"/>
        <stop offset="0.6" stop-color="#e4ecf7"/>
        <stop offset="1" stop-color="#ffffff"/>
      </radialGradient>
    </defs>
    <rect x="10" y="30" width="215" height="215" fill="url(#runnerTone)" role="img" aria-label="Photo: running figure with highlighted joints, faded"/>
    <polyline points="0,2 180,2 180,38" fill="none" stroke="#bdbdbd" stroke-width="2"/>
    <polyline points="0,302 182,302 182,253" fill="none" stroke="#bdbdbd" stroke-width="2"/>
  </svg>
  <svg class="abs" style="left:986px;top:1284px" width="214" height="306">
    <defs>
      <radialGradient id="bottleTone" cx="0.45" cy="0.45" r="0.55">
        <stop offset="0" stop-color="#f7dcb0"/>
        <stop offset="0.55" stop-color="#fbeedd"/>
        <stop offset="1" stop-color="#ffffff"/>
      </radialGradient>
    </defs>
    <rect x="8" y="40" width="200" height="215" fill="url(#bottleTone)" role="img" aria-label="Photo: spilled pill bottle, faded"/>
    <polyline points="214,2 4,2 4,38" fill="none" stroke="#bdbdbd" stroke-width="2"/>
    <polyline points="214,302 2,302 2,253" fill="none" stroke="#bdbdbd" stroke-width="2"/>
  </svg>

  <div class="abs slide-card"></div>
  <svg class="abs" style="left:330px;top:1310px" width="185" height="250">
    <defs>
      <radialGradient id="spineTone" cx="0.45" cy="0.5" r="0.6">
        <stop offset="0" stop-color="#f06a2a"/>
        <stop offset="0.25" stop-color="#8a3a4a"/>
        <stop offset="0.55" stop-color="#1e4aa8"/>
        <stop offset="1" stop-color="#0e2c78"/>
      </radialGradient>
    </defs>
    <path d="M30 248 L30 60 Q40 0 100 5 Q170 10 185 60 L185 248 Z" fill="url(#spineTone)" role="img" aria-label="Illustration: figure with glowing spine showing back pain"/>
  </svg>
  <h3 class="abs slide-title">Pain centres</h3>
  <p class="abs slide-body">It is a long established fact that a reader will be distracted by the readable content of a page when looking at its layout. The point of using Lorem Ipsum is that it has a more-or-less normal distribution of letters, as opposed to using 'Content here, content here', making it look like readable English.</p>
  <div class="abs slide-btn">CONTACT US</div>
  <svg class="abs" style="left:721px;top:1529px" width="22" height="24" aria-hidden="true"><path d="M4 3 L12 14 L9 15 L18 21 M4 3 L3 12" fill="none" stroke="#444" stroke-width="1.3"/></svg>
  <span class="abs chev" style="left:307px;top:1540px">«</span>
  <span class="abs chev" style="left:870px;top:1283px">»</span>

  <div class="abs center-text" style="top:1614px">
    The trustees will initially consider unsolicited applications, for up to £50,000 each, in these areas or related areas.<br>Applications for more substantial project funding will be invited in due course.
  </div>

  <!-- CONTACT -->
  <svg class="abs" style="left:0;top:1730px" width="1200" height="325" aria-hidden="true">
    <defs><linearGradient id="contactBlue" x1="0" y1="0" x2="1" y2="1"><stop offset="0" stop-color="#1f6fe0"/><stop offset="1" stop-color="#1556c6"/></linearGradient></defs>
    <polygon points="378,3 1140,3 830,322 60,322" fill="url(#contactBlue)"/>
    <polygon points="288,17 330,17 288,54" fill="#c8c8c8"/>
    <polygon points="880,298 960,223 960,298" fill="#c8c8c8"/>
  </svg>
  <h2 class="abs section-title contact-title">CONTACT US</h2>
  <p class="abs contact-sub">The Foundation can be contacted by using the contact<br>form below.</p>
  <div class="abs field" style="left:362px;top:1855px">Name *</div>
  <div class="abs field" style="left:613px;top:1855px">Email *</div>
  <div class="abs field" style="left:362px;top:1900px">Phone No *</div>
  <div class="abs field" style="left:613px;top:1900px">Genral Inquary *</div>
  <div class="abs field tall" style="left:362px;top:1945px">Message *</div>
  <div class="abs submit">SUBMIT NOW</div>

  <!-- AIM -->
  <svg class="abs aim-bg" viewBox="0 0 1200 240" role="img" aria-label="Faint background photo of a crowd of people">
    <defs>
      <linearGradient id="crowdBase" x1="0" y1="0" x2="0" y2="1">
        <stop offset="0" stop-color="#ffffff"/>
        <stop offset="1" stop-color="#e8ecf3"/>
      </linearGradient>
      <radialGradient id="crowdWarm" cx="0.7" cy="0.6" r="0.4">
        <stop offset="0" stop-color="#f6e4dc" stop-opacity=".8"/>
        <stop offset="1" stop-color="#f6e4dc" stop-opacity="0"/>
      </radialGradient>
      <radialGradient id="crowdCool" cx="0.2" cy="0.5" r="0.45">
        <stop offset="0" stop-color="#dfe7f4" stop-opacity=".9"/>
        <stop offset="1" stop-color="#dfe7f4" stop-opacity="0"/>
      </radialGradient>
    </defs>
    <rect width="1200" height="240" fill="url(#crowdBase)"/>
    <rect width="1200" height="240" fill="url(#crowdCool)"/>
    <rect width="1200" height="240" fill="url(#crowdWarm)"/>
  </svg>
  <h2 class="abs section-title aim-title">The main aim of Corwenna Foundation is to reduce<br>the suffering caused by chronic pain.</h2>
  <div class="abs aim-btn">CONTACT US</div>

  <!-- FOOTER -->
  <svg class="abs" style="left:0;top:2278px" width="1200" height="377">
    <defs><radialGradient id="footPhoto" cx="0.5" cy="0.45" r="0.5"><stop offset="0" stop-color="#3a2416"/><stop offset="0.6" stop-color="#1a120d"/><stop offset="1" stop-color="#050505"/></radialGradient></defs>
    <rect width="1200" height="377" fill="#050505"/>
    <rect x="200" y="0" width="800" height="377" fill="url(#footPhoto)" role="img" aria-label="Dark faint photo of a human figure with visible nerves"/>
    <polygon points="0,0 1200,0 600,55" fill="#e8ecf3"/>
  </svg>
  <div class="abs brand footer-brand"><span class="brand-mark"></span><span>CORWENNA FOUNDATION</span></div>
  <div class="abs foot-links"><span>Home</span><span>|</span><span>About Us</span><span>|</span><span>Grants</span><span>|</span><span>Contat Us</span></div>
  <div class="abs foot-rule"></div>

  <div class="abs foot-item" style="left:276px">
    <span class="icon-box"><svg width="18" height="20" viewBox="0 0 18 20"><path d="M9 1a6 6 0 0 1 6 6c0 4.5-6 11-6 11S3 11.5 3 7a6 6 0 0 1 6-6z" fill="none" stroke="#fff" stroke-width="1.4"/><circle cx="9" cy="7" r="2.2" fill="none" stroke="#fff" stroke-width="1.4"/></svg></span>
    <span>101 lorem ipsum is dummy<br>printing</span>
  </div>
  <div class="abs foot-item" style="left:531px">
    <span class="icon-box"><svg width="18" height="18" viewBox="0 0 18 18"><path d="M4 1l3 4-2 2c1 2.5 3.5 5 6 6l2-2 4 3-2 3C8 17 1 10 1 4z" fill="#fff"/></svg></span>
    <span>123 456 7890</span>
  </div>
  <div class="abs foot-item" style="left:727px">
    <span class="icon-box"><svg width="20" height="14" viewBox="0 0 20 14"><rect x="1" y="1" width="18" height="12" fill="none" stroke="#fff" stroke-width="1.4"/><path d="M1 1l9 7 9-7M1 13l7-6M19 13l-7-6" fill="none" stroke="#fff" stroke-width="1.2"/></svg></span>
    <span>info@corwennafoundation.org</span>
  </div>

  <div class="abs copy-rule"></div>
  <p class="abs copy">2021 &nbsp;©&nbsp; CORWENNA FOUNDATION -All &nbsp;Right Reserved.</p>
</div>
</body>
</html>
```